Business Management Fortress

Assist with enhancing a powerpoint slide by providing a few design options for consideration. I have a template but open to any creative ideas.

Target Market(s)

Internal employees and stakeholders

Industry/Entity Type

Business Management, Finance, Accounting

Requirements
Must have
• Maintain a fortress, temple, or pyramid schema
Nice to have
• Scenic Background

```html
<!DOCTYPE html>
<html lang="en">
<head>
<meta charset="utf-8">
<title>Business Management Fortress</title>
<link href="https://fonts.googleapis.com/css2?family=Nunito:wght@600;700;800&display=swap" rel="stylesheet">
<style>
  :root{
    --sky-top:#4a8fe0;
    --sky-low:#b3d8f6;
    --sand-top:#eebd6c;
    --sand-low:#d39647;
    --apex-left:#f2c882;
    --apex-right:#e2a862;
    --apex-base:#ebb46c;
    --tier-mid:#cc8a5c;
    --label-dark:#9a5a3a;
    --label-light:#f6dcab;
    --ink-dark:#3a2a1e;
    --ink-light:#fff7ea;
  }
  html,body{margin:0;padding:0;overflow:hidden;background:#fff;}
  .slide{width:1200px;height:675px;position:relative;overflow:hidden;font-family:"Nunito",sans-serif;}
  .slide svg{display:block;}
  .label-dark{fill:var(--label-dark);}
  .label-light{fill:var(--label-light);}
  .text-light{fill:var(--ink-light);font-weight:700;}
  .text-dark{fill:var(--ink-dark);font-weight:700;}
  .slide-code{position:absolute;right:6px;bottom:4px;font-family:Arial,sans-serif;font-size:10px;color:#fff;}
</style>
</head>
<body>
<div class="slide">
  <svg width="1200" height="675" viewBox="0 0 1200 675">
    <defs>
      <linearGradient id="sceneGrad" x1="0" y1="0" x2="0" y2="1">
        <stop offset="0" stop-color="var(--sky-top)"/>
        <stop offset="0.6" stop-color="var(--sky-low)"/>
        <stop offset="0.7" stop-color="var(--sand-top)"/>
        <stop offset="1" stop-color="var(--sand-low)"/>
      </linearGradient>
    </defs>

    <rect class="scene" width="1200" height="675" fill="url(#sceneGrad)" role="img"
      aria-label="Desert scene with three stone pyramids under a blue sky and bright sun, the central pyramid carrying the framework"/>

    <g class="apex">
      <polygon points="619,137 544,222 616,209" fill="var(--apex-left)"/>
      <polygon points="619,137 697,222 616,209" fill="var(--apex-right)"/>
      <polygon points="544,222 616,209 697,222 600,261 566,236" fill="var(--apex-base)"/>
      <text class="text-dark" font-size="13.5" transform="translate(576,214) rotate(-47)">Partner</text>
      <text class="text-dark" font-size="13.5" transform="translate(627,183) rotate(40)">Leader</text>
      <text class="text-dark" font-size="13.5" x="617" y="239" text-anchor="middle">Profitability</text>
    </g>

    <g class="pillars">
      <polygon points="481,290 525,285 518,303 474,304" class="label-dark"/>
      <text class="text-light" font-size="10" x="500" y="298" text-anchor="middle">People</text>
      <polygon points="530,283 592,279 587,298 523,301" class="label-dark"/>
      <text class="text-light" font-size="10.5" x="557" y="294" text-anchor="middle">Innovation</text>
      <polygon points="595,280 665,282 665,304 591,303" class="label-light"/>
      <text class="text-dark" font-size="8.5" x="629" y="290" text-anchor="middle">Business</text>
      <text class="text-dark" font-size="8.5" x="629" y="300" text-anchor="middle">Intelligence</text>
      <polygon points="668,283 755,285 772,306 667,304" class="label-light"/>
      <text class="text-dark" font-size="9.5" x="713" y="298" text-anchor="middle">Strategic Alliances</text>
    </g>

    <g class="foundation">
      <polygon points="621,308 688,392 553,392" fill="var(--tier-mid)"/>
      <text class="text-light" font-size="12" x="621" y="357" text-anchor="middle">Fiduciary</text>
      <text class="text-light" font-size="12" x="621" y="370" text-anchor="middle">Responsibilities</text>

      <polygon points="531,399 601,399 601,419 527,419" class="label-dark"/>
      <text class="text-light" font-size="6" x="565" y="411" text-anchor="middle">Accurate Financials</text>
      <polygon points="601,399 711,399 716,419 601,419" class="label-light"/>
      <text class="text-dark" font-size="6" x="647" y="411" text-anchor="middle">Internal Controls</text>

      <polygon points="522,421 595,421 595,436 518,436" class="label-dark"/>
      <text class="text-light" font-size="6" x="558" y="430" text-anchor="middle">Brand Protection</text>
      <polygon points="595,421 719,421 725,436 595,436" class="label-light"/>
      <text class="text-dark" font-size="6" x="648" y="429" text-anchor="middle">Compliance</text>

      <polygon points="511,442 584,442 584,459 507,459" class="label-dark"/>
      <text class="text-light" font-size="6" x="547" y="452" text-anchor="middle">Ethics</text>
      <polygon points="584,442 743,442 749,459 584,459" class="label-light"/>
      <text class="text-dark" font-size="6" x="646" y="450" text-anchor="middle">Cost Management</text>
    </g>
  </svg>
  <div class="slide-code">C51</div>
</div>
</body>
</html>
```